We are an insurance business, needs your profesinal finishing touch to biz card

California based insurance company. we are providing you the basic elements but need a professional touch to put them together. We want you to wow us. As we have 3 other companies that also need cards and web sites.
Bright Harbor Assurance Group offers the following products;
• Quality of Life Insurance you don’t have to die to use
• Long Term Care (Chronic, Critical & Terminal Illnesses)
• Final/Burial Expense
• Annuities: Fixed & Index
• Qualified & Non-Qualified IRA
• Health Insurance (ACA/Tillman Care)
• Medicare Plans
• Supplemental Benefits: Accident, Disability,
Hospitalization Dental & Vision
Updates

Project Deadline Extended
Reason: Want to allow designers responding to our invites an opportunity to submit their designs.

Target Market(s)

Everybody

Industry/Entity Type

Insurance

Contact Information for Business Card

Please See the Microsoft Word file we uploaded that details ALL that what we need in this project.

Requirements
Must have
• Please See the Microsoft Word file we uploaded that details ALL that what we need in this project.
• NOTE: WE JUST ADDED A $100. BONUS TO "FIRST PLACE"
• Project total budget NOW $230.00
Nice to have
• Your personal touch and creative talent to create a memorable business card for us.
Should not have

```html
<!DOCTYPE html>
<html lang="en">
<head>
<meta charset="utf-8">
<title>Bright Harbor Insurance Service – Business Card</title>
<link rel="stylesheet" href="https://fonts.googleapis.com/css2?family=EB+Garamond:wght@400;500;600&display=swap">
<style>
  :root {
    --page-bg: #e9ecef;
    --navy: #0f3252;
    --sky-top: #a9cdea;
    --sky-bottom: #8fbde2;
    --leaf: #7cb342;
    --ink: #1d2a38;
    --card-white: #ffffff;
    --photo-frame: #c9ccd1;
    --photo-fill: #9a8b84;
    --soft-disc: #eef0f5;
  }
  * { box-sizing: border-box; margin: 0; padding: 0; }
  html, body {
    width: 1200px; height: 900px; overflow: hidden;
    background: var(--page-bg);
    font-family: "EB Garamond", Georgia, serif;
    color: var(--ink);
  }
  .canvas { position: relative; width: 1200px; height: 900px; }

  .card {
    position: absolute; left: 285px; width: 630px; height: 360px;
    overflow: hidden; box-shadow: 0 6px 18px rgba(20, 40, 60, .18);
  }
  .card--back { top: 50px; background: linear-gradient(160deg, var(--sky-top), var(--sky-bottom)); }
  .card--front { top: 480px; background: var(--card-white); }

  .card__band { position: absolute; left: 0; bottom: 0; width: 630px; height: 60px; }
  .card__email {
    position: absolute; right: 18px; bottom: 20px;
    color: #fff; font-size: 17px; letter-spacing: .2px; white-space: nowrap;
  }

  .brand { position: absolute; display: flex; align-items: center; gap: 16px; }
  .brand__dot { width: 64px; height: 64px; border-radius: 50%; background: var(--navy); flex: none; }
  .brand__name { color: var(--navy); font-weight: 500; line-height: 1; }
  .brand__name-main { display: block; font-size: 36px; }
  .brand__name-sub { display: block; font-size: 15px; letter-spacing: 2.5px; text-transform: uppercase; margin-top: 4px; }
  .brand__tagline { display: block; color: var(--ink); font-size: 17px; margin-top: 6px; white-space: nowrap; }

  .card--back .brand { left: 150px; top: 118px; }

  .soft-disc { position: absolute; border-radius: 50%; background: var(--soft-disc); }

  .portrait {
    position: absolute; right: 48px; top: 26px; width: 150px; height: 130px;
    border-radius: 14px; background: var(--photo-frame); padding: 7px;
  }
  .portrait__fill {
    width: 100%; height: 100%; border-radius: 8px;
    background: linear-gradient(180deg, #d9d9db 0%, var(--photo-fill) 60%, #2b2b2f 100%);
  }
  .person {
    position: absolute; right: 13px; top: 166px; width: 220px;
    text-align: center; text-transform: uppercase; white-space: nowrap;
  }
  .person__name { font-size: 17px; font-weight: 500; letter-spacing: 1px; }
  .person__role { font-size: 13px; letter-spacing: 1px; }

  .card--front .brand { left: 40px; top: 120px; }

  .contact {
    position: absolute; left: 70px; top: 236px;
    border-left: 3px solid var(--leaf); padding-left: 12px;
    font-size: 15px; line-height: 1.3; font-style: normal; white-space: nowrap;
  }
</style>
</head>
<body>
<main class="canvas">

  <section class="card card--back" aria-label="Business card back">
    <div class="brand">
      <span class="brand__dot"></span>
      <div>
        <span class="brand__name">
          <span class="brand__name-main">Bright Harbor</span>
          <span class="brand__name-sub">Insurance Service</span>
        </span>
        <span class="brand__tagline">Guarding Family Securing Tomorrow</span>
      </div>
    </div>
    <svg class="card__band" viewBox="0 0 630 60" aria-hidden="true">
      <rect x="0" y="46" width="630" height="14" fill="var(--navy)"/>
      <polygon points="300,8 630,8 630,60 290,60" fill="var(--navy)"/>
      <line x1="292" y1="12" x2="284" y2="46" stroke="#fff" stroke-width="2"/>
    </svg>
    <span class="card__email">dwhitfield@BrightHarborGroupUSA.com</span>
  </section>

  <section class="card card--front" aria-label="Business card front">
    <span class="soft-disc" style="left:300px; top:40px; width:300px; height:300px;"></span>
    <span class="soft-disc" style="left:150px; top:60px; width:140px; height:140px; background:#f2f5ea;"></span>

    <div class="portrait">
      <div class="portrait__fill" role="img" aria-label="Portrait photo of the company president"></div>
    </div>
    <div class="person">
      <div class="person__name">Dana Whitfield</div>
      <div class="person__role">President</div>
    </div>

    <div class="brand">
      <span class="brand__dot"></span>
      <div>
        <span class="brand__name">
          <span class="brand__name-main">Bright Harbor</span>
          <span class="brand__name-sub">Insurance Service</span>
        </span>
        <span class="brand__tagline">Guarding Family Securing Tomorrow</span>
      </div>
    </div>

    <address class="contact">
      2480 Seabright Ave, Ste 120<br>
      Lindenport, CA 90000<br>
      W (555) 014-2231 &bull; M (555) 018-4470
    </address>

    <svg class="card__band" viewBox="0 0 630 60" aria-hidden="true">
      <rect x="0" y="46" width="630" height="14" fill="var(--navy)"/>
      <polygon points="300,8 630,8 630,60 290,60" fill="var(--navy)"/>
      <line x1="292" y1="12" x2="284" y2="46" stroke="#fff" stroke-width="2"/>
    </svg>
    <span class="card__email">dwhitfield@BrightHarborGroupUSA.com</span>
  </section>

</main>
</body>
</html>
```